Redesign of iOS App Lumo Tutor

Redesign of existing App Lumo Tutor, an app that helps learning Japanese Kanjis, Hiragana, Katakana.

The functionallity should remain the same as today: the app is free, you may download it at the app store. But: I like the design of my other apps better ;)

Target Market(s)

Students learning Japanese

Industry/Entity Type

Teacher

Font styles to use
Sans Serif

Requirements
Must have
• Lumo Tutor has 7 main screens, all screens has to be designed for iPhone and iPad: Main, Settings, Reading Tests, Writing Tests, Game, Paper Mode, Search
Nice to have
• I like the logo as it is today

```html
<!DOCTYPE html>
<html lang="en">
<head>
<meta charset="utf-8">
<title>Lumo Tutor – Main Screen</title>
<link rel="stylesheet" href="https://fonts.googleapis.com/css2?family=Roboto:wght@400;500;700&display=swap">
<style>
  :root {
    --page-bg: #eef0f2;
    --status-bg: #000000;
    --status-text: #ffffff;
    --nav-wood-light: #b98753;
    --nav-wood-dark: #8e5f33;
    --nav-line: #6d4525;
    --wood-light: #d9ad78;
    --wood-mid: #b7834f;
    --wood-dark: #7e532d;
    --tile-bg: #9b6a3c;
    --tile-edge: #7a4f2a;
    --card-top: #ffffff;
    --card-bottom: #eceae8;
    --title-color: #7a3f10;
    --desc-color: #8a6a52;
    --accent: #b8743a;
    --icon-light: #f6e9da;
    --icon-soft: #d9b892;
  }
  * { box-sizing: border-box; margin: 0; padding: 0; }
  html, body {
    width: 1000px; height: 1200px; overflow: hidden;
    background: var(--page-bg);
    font-family: "Roboto", Helvetica, Arial, sans-serif;
  }
  .screen {
    position: absolute; left: 162px; top: 0;
    width: 676px; height: 1200px;
    overflow: hidden;
    background: var(--wood-mid);
  }
  .wood-backdrop {
    position: absolute; inset: 131px 0 0 0;
    background: linear-gradient(90deg,
      var(--wood-dark) 0%, var(--wood-mid) 8%, var(--wood-light) 35%,
      #e2b987 50%, var(--wood-light) 65%, var(--wood-mid) 90%, var(--wood-dark) 100%);
  }
  .status-bar {
    position: absolute; top: 0; left: 0; right: 0; height: 50px;
    background: var(--status-bg); color: var(--status-text);
    display: flex; align-items: center; justify-content: space-between;
    padding: 0 16px; font-size: 20px; font-weight: 500;
  }
  .status-left, .status-right { display: flex; align-items: center; gap: 8px; width: 200px; }
  .status-right { justify-content: flex-end; }
  .signal { display: flex; gap: 3px; }
  .signal span { width: 10px; height: 10px; border-radius: 50%; background: var(--status-text); }
  .battery { width: 40px; height: 18px; border-radius: 3px; background: var(--status-text); position: relative; }
  .battery::after { content: ""; position: absolute; right: -4px; top: 6px; width: 3px; height: 6px; background: var(--status-text); border-radius: 0 2px 2px 0; }
  .nav-bar {
    position: absolute; top: 50px; left: 0; right: 0; height: 81px;
    background: linear-gradient(180deg, var(--nav-wood-light), var(--nav-wood-dark));
    border-bottom: 3px solid var(--nav-line);
    display: flex; align-items: center; justify-content: center;
  }
  .menu-button {
    position: absolute; left: 28px; top: 16px; width: 70px; height: 46px;
    background: rgba(120, 70, 30, 0.45); border-radius: 3px;
    display: flex; align-items: center; justify-content: center;
  }
  .app-title { color: #ffffff; font-weight: 700; font-size: 34px; letter-spacing: 1px; }
  .menu-list {
    position: absolute; top: 171px; left: 38px; width: 600px;
    list-style: none; display: flex; flex-direction: column; gap: 19px;
  }
  .menu-item { display: flex; height: 134px; box-shadow: 0 3px 6px rgba(60, 30, 10, 0.35); }
  .menu-icon {
    width: 152px; flex: none;
    background: linear-gradient(180deg, #a87343, var(--tile-bg));
    border-right: 2px solid var(--tile-edge);
    display: flex; align-items: center; justify-content: center;
  }
  .icon-art {
    width: 72px; height: 72px; border-radius: 6px;
    background: linear-gradient(160deg, var(--icon-light), var(--icon-soft));
  }
  .menu-card {
    flex: 1; position: relative;
    background: linear-gradient(180deg, var(--card-top), var(--card-bottom));
    padding: 26px 80px 0 22px;
  }
  .menu-title { color: var(--title-color); font-size: 27px; font-weight: 400; margin-bottom: 8px; }
  .menu-desc { color: var(--desc-color); font-size: 15.5px; line-height: 19px; }
  .chevron { position: absolute; right: 18px; top: 50%; transform: translateY(-50%); }
</style>
</head>
<body>
<main class="screen">
  <div class="wood-backdrop" role="img" aria-label="Wooden plank background texture"></div>

  <header class="status-bar">
    <div class="status-left">
      <div class="signal"><span></span><span></span><span></span><span></span><span></span></div>
      <span>NOVA</span>
      <svg width="22" height="16" viewBox="0 0 22 16" aria-hidden="true">
        <path d="M1 5 A14 14 0 0 1 21 5" stroke="#fff" stroke-width="2.5" fill="none"/>
        <path d="M5 9 A8 8 0 0 1 17 9" stroke="#fff" stroke-width="2.5" fill="none"/>
        <circle cx="11" cy="13.5" r="2.2" fill="#fff"/>
      </svg>
    </div>
    <span class="status-time">4:21 PM</span>
    <div class="status-right">
      <svg width="12" height="20" viewBox="0 0 12 20" aria-hidden="true">
        <path d="M1 6 L11 14 L6 18 V2 L11 6 L1 14" stroke="#888" stroke-width="1.6" fill="none"/>
      </svg>
      <span>100%</span>
      <span class="battery"></span>
    </div>
  </header>

  <nav class="nav-bar">
    <div class="menu-button" aria-label="Menu">
      <svg width="32" height="26" viewBox="0 0 32 26" aria-hidden="true">
        <g fill="#fff">
          <rect x="0" y="1" width="5" height="4"/><rect x="8" y="1" width="24" height="4"/>
          <rect x="0" y="8" width="5" height="4"/><rect x="8" y="8" width="24" height="4"/>
          <rect x="0" y="15" width="5" height="4"/><rect x="8" y="15" width="24" height="4"/>
          <rect x="0" y="22" width="5" height="4"/><rect x="8" y="22" width="24" height="4"/>
        </g>
      </svg>
    </div>
    <h1 class="app-title">Lumo Tutor</h1>
  </nav>

  <ul class="menu-list">
    <li class="menu-item">
      <div class="menu-icon"><div class="icon-art" role="img" aria-label="Dictionary illustration: book with a kanji"></div></div>
      <div class="menu-card">
        <h2 class="menu-title">Dictionary</h2>
        <p class="menu-desc">In enim molestie ea blandit facilisis consequat et vero, ut zzril lorem ipsum</p>
        <svg class="chevron" width="26" height="38" viewBox="0 0 26 38" aria-hidden="true">
          <path d="M5 5 L20 19 L5 33" stroke="var(--accent)" stroke-width="9" stroke-linecap="round" stroke-linejoin="round" fill="none"/>
        </svg>
      </div>
    </li>
    <li class="menu-item">
      <div class="menu-icon"><div class="icon-art" role="img" aria-label="Writing illustration: kanji sheet and brush"></div></div>
      <div class="menu-card">
        <h2 class="menu-title">Learn to Write</h2>
        <p class="menu-desc">In enim molestie ea blandit facilisis consequat et vero, ut zzril lorem ipsum</p>
        <svg class="chevron" width="26" height="38" viewBox="0 0 26 38" aria-hidden="true">
          <path d="M5 5 L20 19 L5 33" stroke="var(--accent)" stroke-width="9" stroke-linecap="round" stroke-linejoin="round" fill="none"/>
        </svg>
      </div>
    </li>
    <li class="menu-item">
      <div class="menu-icon"><div class="icon-art" role="img" aria-label="Test illustration: hiragana character"></div></div>
      <div class="menu-card">
        <h2 class="menu-title">Kanji Test</h2>
        <p class="menu-desc">In enim molestie ea blandit facilisis consequat et vero, ut zzril lorem ipsum</p>
        <svg class="chevron" width="26" height="38" viewBox="0 0 26 38" aria-hidden="true">
          <path d="M5 5 L20 19 L5 33" stroke="var(--accent)" stroke-width="9" stroke-linecap="round" stroke-linejoin="round" fill="none"/>
        </svg>
      </div>
    </li>
    <li class="menu-item">
      <div class="menu-icon"><div class="icon-art" role="img" aria-label="Game illustration: stylised question mark"></div></div>
      <div class="menu-card">
        <h2 class="menu-title">Game</h2>
        <p class="menu-desc">In enim molestie ea blandit facilisis consequat et vero, ut zzril lorem ipsum</p>
        <svg class="chevron" width="26" height="38" viewBox="0 0 26 38" aria-hidden="true">
          <path d="M5 5 L20 19 L5 33" stroke="var(--accent)" stroke-width="9" stroke-linecap="round" stroke-linejoin="round" fill="none"/>
        </svg>
      </div>
    </li>
  </ul>
</main>
</body>
</html>
```